Painting business fun and professional website

Looking for a website design that is easy to navigate, attractive, energetic, and professional. Include categories/pages: About, Residential, Commercial, Etc.

Target Market(s)

Home owners, Property managers, builders, maintenance supervisors, etc.

Industry/Entity Type

painting, construction

Number of Pages Required

4 page

Font styles to use
Other font styles liked:
• This font for categories, but not all the literature.Latino www.quorbatype.net/fonts/a-velmora

Colors
0094D4
00A9DD
6FCCEA
C7EBF8
E9F6FB
FFF300
FFF600
FEFA6F
FFFEC7
FFFEE8
EB3D1F
EC4F4E
F09395
F8D3D4
FCEDEE

Requirements
Must have
• Connect with social media handles, short transformation videos, photos, Quick Quote request. Colors Red (R247 G32 B0 #f72300 C0 M98 Y93 K0), Blue (R0, G204, B255 #00CCFF C65 M0 Y0 K0) Yellow (R255, G255, B0 #FFE100 C2 M7 Y100 K0)
Nice to have
• Website design to stand out from other painting business websites in a fun and modern way. Nothing stale, boring, or basic please

```html
<!DOCTYPE html>
<html lang="en">
<head>
<meta charset="utf-8">
<title>Brisk Painting, LLC</title>
<link rel="stylesheet" href="https://fonts.googleapis.com/css2?family=Montserrat:wght@400;500;600;700;800;900&family=Mulish:wght@400;600;700&display=swap">
<style>
:root{
  --blue:#1ec0f5;
  --blue-deep:#0094d4;
  --yellow:#ffe100;
  --ink:#1d1d1f;
  --text:#555a60;
  --grey:#efefef;
  --dark:#1f2327;
  --white:#ffffff;
  --star:#f59a1a;
}
*{box-sizing:border-box;margin:0;padding:0}
html,body{width:1200px;height:4751px;overflow:hidden}
body{position:relative;background:var(--white);font-family:'Mulish',sans-serif;color:var(--text)}
.abs{position:absolute}
.btn{position:absolute;background:var(--yellow);color:var(--ink);font-family:'Montserrat',sans-serif;font-weight:700;display:flex;align-items:center;justify-content:center;text-transform:uppercase}

/* header */
.topbar{left:0;top:0;width:1200px;height:114px;background:var(--blue)}
.logo-panel{left:0;top:0}
.brand{display:flex;align-items:center;gap:10px;font-family:'Montserrat',sans-serif;font-weight:800;color:var(--ink)}
.brand .dot{border-radius:50%;background:var(--yellow);flex:none}
.follow{left:498px;top:31px;color:#fff;font-family:'Montserrat',sans-serif;font-size:11px;font-weight:500;display:flex;align-items:center;gap:8px}
.follow i{display:block;width:22px;height:22px;border-radius:50%;background:#fff}
.call-outline{left:713px;top:22px;width:173px;height:33px;border:1.5px solid #fff;color:#fff;font-family:'Montserrat',sans-serif;font-size:11px;font-weight:500;display:flex;align-items:center;justify-content:center}
.call-phone{left:918px;top:22px;width:147px;height:33px;font-size:12px;font-weight:500;text-transform:none;gap:6px}
.nav{font-family:'Montserrat',sans-serif;font-size:11.5px;font-weight:600;color:#fff}
.nav a{color:#fff;text-decoration:none;position:absolute;white-space:nowrap}
.nav a.active::after{content:"";position:absolute;left:0;right:0;bottom:-6px;height:2px;background:#fff}

/* hero */
.hero{left:0;top:114px;width:1200px;height:580px;background:linear-gradient(180deg,#cfe4f2 0%,#a9c9a0 40%,#8c8c78 60%,#5f7d3e 85%,#4a6a2e 100%)}
.hero-title{left:0;top:152px;width:1200px;text-align:center;font-family:'Montserrat',sans-serif;color:#2a2a2a}
.hero-title b{display:block;font-size:24px;font-weight:800;letter-spacing:.3px}
.hero-title span{display:block;font-size:23px;font-weight:400;margin-top:4px;letter-spacing:.5px}
.hero-btn{left:501px;top:234px;width:197px;height:39px;font-size:13px}
.slide-arrow{top:345px;width:44px;height:46px;background:#fff;display:flex;align-items:center;justify-content:center}

/* section titles */
.title-row{left:0;width:1200px;display:flex;justify-content:center}
.section-title{display:inline-block;background:var(--blue);color:var(--white);font-family:'Montserrat',sans-serif;font-weight:800;font-size:18px;letter-spacing:.8px;text-transform:uppercase;padding:11px 26px;border-radius:24px;white-space:nowrap;line-height:1.2}

/* services */
.card{width:289px;height:419px;background:#fff;box-shadow:0 4px 18px rgba(0,0,0,.12)}
.card .ph{height:199px}
.card h3{position:absolute;left:31px;top:232px;font-family:'Montserrat',sans-serif;font-size:13px;font-weight:600;color:var(--ink)}
.card p{position:absolute;left:31px;top:265px;width:225px;font-size:10.5px;line-height:16px}
.card .btn{left:31px;top:358px;width:89px;height:28px;font-size:9px}

/* about */
.grey-band{left:0;width:1200px;background:var(--grey)}
.about-img{left:133px;top:1434px;width:472px;height:301px;border-radius:150px;background:linear-gradient(160deg,#b8d6ee,#e8ecee 45%,#7c8a6a 80%,#4f6a3a)}
.about-text{left:665px;top:1508px;width:402px;font-size:12.6px;line-height:20.6px;text-align:justify}

/* why */
.why-img{left:0;top:1981px;width:546px;height:428px;border-radius:0 60px 60px 0;background:linear-gradient(135deg,#e9e9e6,#cfd0cc 45%,#2b8fd6 70%,#1d70b8)}
.feature{left:588px;width:480px;height:80px}
.feature .ic{position:absolute;left:0;top:0;width:66px;height:66px;border-radius:50%;background:var(--blue);display:flex;align-items:center;justify-content:center}
.feature h4{position:absolute;left:92px;top:0;font-family:'Montserrat',sans-serif;font-size:13px;font-weight:700;color:var(--ink)}
.feature p{position:absolute;left:92px;top:22px;width:388px;font-size:10.7px;line-height:16px}
.side-bar{left:1193px;top:1981px;width:7px;height:428px;background:var(--yellow)}

/* testimonials */
.tcard{top:2632px;width:295px;height:330px;background:#fff}
.tcard .q{position:absolute;left:50px;top:22px;font-family:'Montserrat',sans-serif;font-size:40px;font-weight:900;color:var(--blue);line-height:1}
.tcard .stars{position:absolute;left:50px;top:48px;color:var(--star);font-size:12px;letter-spacing:1px}
.tcard p{position:absolute;left:50px;top:82px;width:220px;font-size:10.6px;line-height:16.5px}
.tcard .who{position:absolute;left:50px;top:270px;display:flex;align-items:center;gap:10px;font-size:10.5px;color:var(--ink)}
.tcard .who i{display:block;width:38px;height:38px;border-radius:50%;background:linear-gradient(#e8d8c8,#b89a80)}
.tcard .who small{display:block;font-size:9px;color:var(--text)}
.circ-arrow{top:2776px;width:28px;height:28px;border:1.5px solid #444;border-radius:50%;display:flex;align-items:center;justify-content:center}

/* before after */
.ba{width:292px;height:196px;display:flex}
.ba div{flex:1}
.ba .tag{position:absolute;background:#fff;font-family:'Montserrat',sans-serif;font-size:9.5px;color:#555;padding:4px 8px;letter-spacing:.3px}
.ba .tag.b{left:0;top:14px}
.ba .tag.a{right:0;bottom:14px}

/* estimate */
.dark{left:0;top:3686px;width:1200px;height:737px;background:linear-gradient(180deg,#23272b 0%,#1b1f22 55%,#2a2f2a 85%,#1c201d 100%)}
.est-title{left:0;top:3764px;width:1200px;text-align:center;font-family:'Montserrat',sans-serif;font-size:19px;font-weight:600;color:#fff;letter-spacing:.5px}
.lbl{font-family:'Montserrat',sans-serif;font-size:11px;color:#ddd}
.inp{background:#fff}
.submit{left:549px;top:4337px;width:120px;height:38px;font-size:15px;font-weight:800;text-transform:uppercase}

/* footer */
.f-head{font-family:'Montserrat',sans-serif;font-size:12px;font-weight:700;color:var(--ink)}
.f-item{display:flex;gap:14px;align-items:flex-start;font-size:11px;line-height:16px;color:#444}
.f-item i{flex:none;width:22px;height:22px;border-radius:50%;background:var(--yellow);display:flex;align-items:center;justify-content:center}
.f-menu{font-family:'Montserrat',sans-serif;font-size:11px;color:#444;line-height:24.5px}
.rule{left:122px;top:4676px;width:934px;height:1px;background:#999}
.copy{left:0;top:4708px;width:1200px;text-align:center;font-size:9.5px;color:#444}
</style>
</head>
<body>

<!-- header -->
<div class="abs topbar"></div>
<svg class="abs logo-panel" width="420" height="114" viewBox="0 0 420 114" aria-hidden="true">
  <path d="M0 0H340C372 20 402 60 415 114H0Z" fill="#8fdcf7"/>
  <path d="M0 0H320C350 22 378 62 388 114H0Z" fill="#ffffff"/>
</svg>
<div class="abs brand" style="left:140px;top:62px;font-size:21px;line-height:1.05">
  <span class="dot" style="width:34px;height:34px"></span>
  <span>Brisk<br>Painting, LLC</span>
</div>
<div class="abs follow">Follow Us <i></i><i></i><i></i></div>
<div class="abs call-outline">Call For a FREE Estimate</div>
<div class="btn call-phone">
  <svg width="14" height="14" viewBox="0 0 24 24"><path d="M6.6 10.8a15 15 0 006.6 6.6l2.2-2.2a1 1 0 011-.25 11 11 0 003.5.56 1 1 0 011 1V20a1 1 0 01-1 1A17 17 0 013 4a1 1 0 011-1h3.5a1 1 0 011 1 11 11 0 00.56 3.5 1 1 0 01-.25 1z" fill="#1d1d1f"/></svg>
  +1 555 014 2290
</div>
<nav class="abs nav" style="left:0;top:78px;width:1200px">
  <a class="active" style="left:499px">HOME</a>
  <a style="left:570px">ABOUT</a>
  <a style="left:653px">RESIDENTIAL</a>
  <a style="left:772px">COMMERCIAL</a>
  <a style="left:896px">GALLERY</a>
  <a style="left:984px">CONTACT US</a>
</nav>

<!-- hero -->
<div class="abs hero" role="img" aria-label="Large two-storey grey house with white porch, green lawn and trees"></div>
<svg class="abs" style="left:0;top:640px" width="1200" height="60" viewBox="0 0 1200 60" aria-hidden="true">
  <path d="M0 38C120 14 230 34 360 22S620 6 760 20 1000 30 1090 14 1180 10 1200 16V60H0Z" fill="#ffffff"/>
  <path d="M0 38C120 14 230 34 360 22S620 6 760 20 1000 30 1090 14 1180 10 1200 16" fill="none" stroke="#ffe100" stroke-width="2"/>
</svg>
<div class="abs hero-title"><b>THE RIGHT INTERIOR AND</b><span>EXTERIOR PAINTING FOR YOU</span></div>
<div class="btn hero-btn">Get a free estimate</div>
<div class="abs slide-arrow" style="left:0;border-radius:0 23px 23px 0"><svg width="10" height="16" viewBox="0 0 10 16"><path d="M8 2L2 8l6 6" fill="none" stroke="#222" stroke-width="2"/></svg></div>
<div class="abs slide-arrow" style="left:1156px;border-radius:23px 0 0 23px"><svg width="10" height="16" viewBox="0 0 10 16"><path d="M2 2l6 6-6 6" fill="none" stroke="#222" stroke-width="2"/></svg></div>

<!-- services -->
<div class="abs title-row" style="top:734px"><h2 class="section-title">Our Services</h2></div>

<div class="abs card" style="left:131px;top:831px">
  <div class="ph" role="img" aria-label="Modern dark home with pool at dusk" style="background:linear-gradient(160deg,#9cb8d4,#2e3236 55%,#6a7a5a)"></div>
  <h3>RESIDENTIAL</h3>
  <p>There are many variations of passages of Lorem Ipsum available, but the major ity have suffered alteration in some form, by injected humour, or randomised</p>
  <div class="btn">Read more</div>
</div>
<div class="abs card" style="left:455px;top:831px">
  <div class="ph" role="img" aria-label="Glass office towers against blue sky" style="background:linear-gradient(170deg,#cfe3f3,#6b8aa6 50%,#7a5a48)"></div>
  <h3>COMMERCIAL</h3>
  <p>There are many variations of passages of Lorem Ipsum available, but the major ity have suffered alteration in some form, by injected humour, or randomised</p>
  <div class="btn">Read more</div>
</div>
<div class="abs card" style="left:776px;top:831px">
  <div class="ph" role="img" aria-label="Grey house with white trim and green lawn" style="background:linear-gradient(175deg,#4d8ed0,#b8c6cf 45%,#6c8a52)"></div>
  <h3>EXTERIOR</h3>
  <p>There are many variations of passages of Lorem Ipsum available, but the major ity have suffered alteration in some form, by injected humour, or randomised</p>
  <div class="btn">Read more</div>
</div>

<!-- about -->
<svg class="abs" style="left:0;top:1300px" width="1200" height="40" viewBox="0 0 1200 40" aria-hidden="true">
  <path d="M0 30C150 22 300 34 480 18S760 4 900 16 1100 26 1200 20V40H0Z" fill="#efefef"/>
</svg>
<div class="abs grey-band" style="top:1336px;height:465px"></div>
<div class="abs about-img" role="img" aria-label="White modern farmhouse with black window frames"></div>
<div class="abs" style="left:663px;top:1420px"><h2 class="section-title">About Brisk Painting LLC</h2></div>
<p class="abs about-text">Sed ut perspiciatis unde omnis iste natus error sit voluptatem accusantium doloremque laudantium, totam rem aperiam, eaque ipsa quae ab illo inventore veritatis et quasi architecto beatae vitae dicta sunt explicabo. Nemo enim ipsam voluptatem quia voluptas sit aspernatur aut odit aut fugit, sed quia consequuntur magni dolores eos qui ratione voluptatem sequi nesciunt. Neque porro quisquam est, qui dolorem ipsum quia dolor sit amet, consectetur, adipisci velit, sed quia non numquam eius modi tempora incidunt ut labore et dolore magnam aliquam quaera</p>
<div class="btn" style="left:663px;top:1721px;width:89px;height:27px;font-size:9px">Read more</div>

<!-- why choose us -->
<div class="abs title-row" style="top:1864px"><h2 class="section-title">Why Choose Us</h2></div>
<div class="abs why-img" role="img" aria-label="Painter in blue cap rolling white paint onto a ceiling"></div>
<div class="abs side-bar"></div>

<div class="abs feature" style="top:1985px">
  <div class="ic"><svg width="30" height="30" viewBox="0 0 30 30"><rect x="4" y="4" width="20" height="8" rx="2" fill="#fff"/><path d="M24 8h3v7H15v4" fill="none" stroke="#fff" stroke-width="2"/><rect x="12.5" y="19" width="5" height="9" rx="1" fill="#fff"/></svg></div>
  <h4>OVER 15 YEARS OF EXPERIENCE</h4>
  <p>There are many variations of passages of Lorem Ipsum available, but the major ity have suffered alteration in some form, by injected humour, or randomised</p>
</div>
<div class="abs feature" style="top:2097px">
  <div class="ic"><svg width="30" height="30" viewBox="0 0 30 30"><path d="M3 14L15 4l12 10" fill="none" stroke="#fff" stroke-width="2.5"/><rect x="7" y="14" width="16" height="12" fill="#fff"/><rect x="12" y="18" width="6" height="8" fill="#1ec0f5"/></svg></div>
  <h4>PROFESSIONAL RESULTS</h4>
  <p>There are many variations of passages of Lorem Ipsum available, but the major ity have suffered alteration in some form, by injected humour, or randomised</p>
</div>
<div class="abs feature" style="top:2214px">
  <div class="ic"><svg width="30" height="30" viewBox="0 0 30 30"><rect x="4" y="13" width="5" height="13" fill="#fff"/><path d="M11 13l5-9c2 0 3 1 3 3l-1 5h7c1.5 0 2.5 1.5 2 3l-2.5 9c-.3 1-1 2-2.5 2H11Z" fill="#fff"/></svg></div>
  <h4>HONEST AND DEPENDABLE</h4>
  <p>There are many variations of passages of Lorem Ipsum available, but the major ity have suffered alteration in some form, by injected humour, or randomised</p>
</div>
<div class="abs feature" style="top:2336px">
  <div class="ic"><svg width="30" height="30" viewBox="0 0 30 30"><path d="M6 16v-3a9 9 0 0118 0v3" fill="none" stroke="#fff" stroke-width="2.5"/><rect x="4" y="15" width="5" height="8" rx="2" fill="#fff"/><rect x="21" y="15" width="5" height="8" rx="2" fill="#fff"/><circle cx="15" cy="15" r="4" fill="#fff"/><path d="M8 28c1-4 4-6 7-6s6 2 7 6Z" fill="#fff"/></svg></div>
  <h4>SUPPORT</h4>
  <p>There are many variations of passages of Lorem Ipsum available, but the major ity have suffered alteration in some form, by injected humour, or randomised</p>
</div>

<!-- testimonials -->
<svg class="abs" style="left:0;top:2470px" width="1200" height="40" viewBox="0 0 1200 40" aria-hidden="true">
  <path d="M0 26C160 18 330 32 520 20S820 8 980 18 1140 24 1200 20V40H0Z" fill="#efefef"/>
</svg>
<div class="abs grey-band" style="top:2506px;height:504px"></div>
<div class="abs title-row" style="top:2534px"><h2 class="section-title">Testimonials</h2></div>

<div class="abs tcard" style="left:129px">
  <div class="q">&ldquo;</div><div class="stars">&#9733;&#9733;&#9733;&#9733;&#9733;</div>
  <p>There are many variations of pas sages of Lorem Ipsum ava ilable, but the majority have suffered alter ation in some form, by inject ed humour, or randomised words whi ch don't look even slightly believ able. If you are going to use a pass age of Lorem Ipsum, you need to be sure there isn't anything emba rrassing hidden in the middle of text. All the Lorem.</p>
  <div class="who"><i></i><div>Daniel<small>Fairview</small></div></div>
</div>
<div class="abs tcard" style="left:455px">
  <div class="q">&ldquo;</div>
  <p>There are many variations of pas sages of Lorem Ipsum ava ilable, but the majority have suffered alter ation in some form, by inject ed humour, or randomised words whi ch don't look even slightly believ able. If you are going to use a pass age of Lorem Ipsum, you need to be sure there isn't anything emba rrassing hidden in the middle of text. All the Lorem.</p>
  <div class="who"><i></i><div>Daniel<small>Fairview</small></div></div>
</div>
<div class="abs tcard" style="left:774px">
  <div class="q">&ldquo;</div>
  <p>There are many variations of pas sages of Lorem Ipsum ava ilable, but the majority have suffered alter ation in some form, by inject ed humour, or randomised words whi ch don't look even slightly believ able. If you are going to use a pass age of Lorem Ipsum, you need to be sure there isn't anything emba rrassing hidden in the middle of text. All the Lorem.</p>
  <div class="who"><i></i><div>Daniel<small>Fairview</small></div></div>
</div>
<div class="abs circ-arrow" style="left:68px"><svg width="8" height="12" viewBox="0 0 8 12"><path d="M6 1L1 6l5 5" fill="none" stroke="#444" stroke-width="1.6"/></svg></div>
<div class="abs circ-arrow" style="left:1095px"><svg width="8" height="12" viewBox="0 0 8 12"><path d="M2 1l5 5-5 5" fill="none" stroke="#444" stroke-width="1.6"/></svg></div>

<!-- before & after -->
<div class="abs title-row" style="top:3069px"><h2 class="section-title">Before &amp; After</h2></div>

<div class="abs ba" style="left:131px;top:3164px" role="img" aria-label="Room with bare plaster walls beside the same room freshly painted white">
  <div style="background:linear-gradient(160deg,#a48a66,#6f5a44 60%,#3d6a9a)"></div><div style="background:linear-gradient(160deg,#f4f4f2,#e0dfdc 60%,#a06a3e)"></div>
  <span class="tag b">BEFORE</span><span class="tag a">AFTER</span></div>
<div class="abs ba" style="left:448px;top:3164px" role="img" aria-label="Stained hallway wall beside the same hallway repainted grey">
  <div style="background:linear-gradient(160deg,#8a7e5c,#5e5640)"></div><div style="background:linear-gradient(160deg,#8c8a80,#6d6a60 70%,#8a6a4a)"></div>
  <span class="tag b">BEFORE</span><span class="tag a">AFTER</span></div>
<div class="abs ba" style="left:769px;top:3164px" role="img" aria-label="Unfinished room with ladder beside the same room painted sage green">
  <div style="background:linear-gradient(160deg,#d6d8d4,#a8a49a 60%,#6a4a34)"></div><div style="background:linear-gradient(160deg,#b8c4b0,#98a890 60%,#6a4028)"></div>
  <span class="tag b">BEFORE</span><span class="tag a">AFTER</span></div>
<div class="abs ba" style="left:131px;top:3378px" role="img" aria-label="Worn brick room beside the same room renovated in white">
  <div style="background:linear-gradient(160deg,#7a5a44,#4a3a30 60%,#2e4a6a)"></div><div style="background:linear-gradient(160deg,#f6f6f4,#e4e4e0 60%,#9a6a44)"></div>
  <span class="tag b">BEFORE</span><span class="tag a">AFTER</span></div>
<div class="abs ba" style="left:448px;top:3378px" role="img" aria-label="Bare room with ladder beside the same room painted turquoise">
  <div style="background:linear-gradient(160deg,#e8e8e6,#c8c6c0 60%,#5a4a3a)"></div><div style="background:linear-gradient(160deg,#6cc8b4,#4ab09c 60%,#8a5a3a)"></div>
  <span class="tag b">BEFORE</span><span class="tag a">AFTER</span></div>
<div class="abs ba" style="left:769px;top:3378px" role="img" aria-label="Stripped kitchen beside the same kitchen with new white cabinets">
  <div style="background:linear-gradient(160deg,#c8ccd0,#9aa0a8 60%,#b8b8b8)"></div><div style="background:linear-gradient(160deg,#f2f2f2,#d8d8da 60%,#bcbcbe)"></div>
  <span class="tag b">BEFORE</span><span class="tag a">AFTER</span></div>

<div class="btn" style="left:533px;top:3605px;width:134px;height:33px;font-size:9.5px">View all images</div>

<!-- estimate -->
<div class="abs dark" role="img" aria-label="House exterior at night, darkened behind the form"></div>
<svg class="abs" style="left:0;top:3660px" width="1200" height="40" viewBox="0 0 1200 40" aria-hidden="true">
  <path d="M0 30C140 18 300 34 500 22S820 6 980 16 1140 28 1200 24V40H0Z" fill="#23272b"/>
</svg>
<div class="abs est-title">GET A FREE ESTIMATE</div>

<div class="abs lbl" style="left:280px;top:3859px">First Name *</div>
<div class="abs lbl" style="left:607px;top:3859px">Last Name *</div>
<div class="abs inp" style="left:280px;top:3881px;width:309px;height:39px"></div>
<div class="abs inp" style="left:607px;top:3881px;width:309px;height:39px"></div>
<div class="abs lbl" style="left:280px;top:3939px">Phone *</div>
<div class="abs lbl" style="left:607px;top:3939px">Email</div>
<div class="abs inp" style="left:280px;top:3961px;width:309px;height:39px"></div>
<div class="abs inp" style="left:607px;top:3961px;width:309px;height:39px"></div>
<div class="abs lbl" style="left:280px;top:4020px">Address *</div>
<div class="abs inp" style="left:280px;top:4044px;width:640px;height:37px"></div>
<div class="abs lbl" style="left:280px;top:4099px">City *</div>
<div class="abs lbl" style="left:498px;top:4099px">State *</div>
<div class="abs lbl" style="left:719px;top:4099px">Zipcode *</div>
<div class="abs inp" style="left:280px;top:4123px;width:199px;height:37px"></div>
<div class="abs inp" style="left:498px;top:4123px;width:199px;height:37px"></div>
<div class="abs inp" style="left:719px;top:4123px;width:201px;height:37px"></div>
<div class="abs lbl" style="left:280px;top:4177px">How can we help you?</div>
<div class="abs inp" style="left:280px;top:4202px;width:640px;height:100px"></div>
<div class="btn submit">Submit</div>

<!-- footer -->
<div class="abs brand" style="left:130px;top:4522px;font-size:26px;line-height:1.05">
  <span class="dot" style="width:42px;height:42px"></span>
  <span>Brisk<br>Painting, LLC</span>
</div>

<div class="abs f-head" style="left:415px;top:4462px">CONTACT US</div>
<div class="abs f-item" style="left:415px;top:4495px">
  <i><svg width="10" height="12" viewBox="0 0 10 12"><path d="M5 0a4 4 0 014 4c0 3-4 8-4 8S1 7 1 4a4 4 0 014-4z" fill="#1d1d1f"/><circle cx="5" cy="4" r="1.5" fill="#ffe100"/></svg></i>
  <span>Unit 12, Harbor Court,<br>240 Larkspur Road, Fairview 4410.</span>
</div>
<div class="abs f-item" style="left:415px;top:4545px">
  <i><svg width="11" height="11" viewBox="0 0 24 24"><path d="M6.6 10.8a15 15 0 006.6 6.6l2.2-2.2a1 1 0 011-.25 11 11 0 003.5.56 1 1 0 011 1V20a1 1 0 01-1 1A17 17 0 013 4a1 1 0 011-1h3.5a1 1 0 011 1 11 11 0 00.56 3.5 1 1 0 01-.25 1z" fill="#1d1d1f"/></svg></i>
  <span>Call Us<br>+1 555 014 2290</span>
</div>
<div class="abs f-item" style="left:415px;top:4597px">
  <i><svg width="11" height="9" viewBox="0 0 12 9"><rect x=".5" y=".5" width="11" height="8" fill="none" stroke="#1d1d1f"/><path d="M.5.5L6 5l5.5-4.5" fill="none" stroke="#1d1d1f"/></svg></i>
  <span>E mail Us<br>hello@briskpainting.co</span>
</div>

<div class="abs f-head" style="left:778px;top:4462px">MENU</div>
<div class="abs f-menu" style="left:778px;top:4485px">HOME<br>ABOUT<br>RESIDENTIAL<br>COMMERCIAL<br>GALLERY<br>CONTACT US</div>

<div class="abs f-head" style="left:958px;top:4462px">FOLLOW US</div>
<div class="abs f-item" style="left:958px;top:4494px"><i></i><span>Like us on<br>PAGEBOOK</span></div>
<div class="abs f-item" style="left:958px;top:4545px"><i></i><span>Follow us on<br>CHIRPER</span></div>
<div class="abs f-item" style="left:958px;top:4596px"><i></i><span>Follow us on<br>WORKLINK</span></div>

<div class="abs rule"></div>
<div class="abs copy">Copyright © 2023 All Rights Reserved</div>

</body>
</html>
```